Bref créative
Tri Fold Product Flyer
Lightning Photography Device
Built for every bold vision.
We need a flyer for trade shows for an automated shutter release system for photographing lightning strikes and fireworks.
Go to www.drevasystems.example for more information about the device. The device is called the Sky Moth™.
Photography
Amateur and professional nature photographers.
Tri-fold flyer, 8.5" X 11" before folding.
This is our company logo.
Images of the Sky Moth™ device.
More images of the Sky Moth™ device. Other images are available, please ask.
These are some images take with the Sky Moth™. Some or all of them should be included on the brochure.
Higher res file for final draft for #15.

```html
<!DOCTYPE html>
<html lang="en">
<head>
<meta charset="utf-8">
<title>DT Drevas – Sky Moth Tri-Fold Flyer</title>
<link rel="stylesheet" href="https://fonts.googleapis.com/css2?family=Open+Sans:wght@400;600;700&display=swap">
<style>
:root{
  --stage:#e9e9e9;
  --stage-light:#f6f6f6;
  --ink:#141414;
  --panel:#1c1c1c;
  --panel-2:#242424;
  --orange:#f29a1a;
  --orange-deep:#d97a0a;
  --text-light:#cfcfcf;
  --text-dim:#8d8d8d;
  --brand-grey:#8a8a8a;
  --white:#ffffff;
}
*{box-sizing:border-box;margin:0;padding:0}
html,body{width:1200px;height:694px;overflow:hidden}
body{
  font-family:"Open Sans",Arial,sans-serif;
  background:radial-gradient(ellipse at 50% 30%,var(--stage-light) 0%,var(--stage) 70%);
  position:relative;color:var(--text-light);
}
.brand{position:absolute;left:0;width:1200px;top:26px;text-align:center}
.brand-mark{display:block;width:54px;height:54px;margin:0 auto;background:var(--orange)}
.brand-name{display:block;margin-top:36px;font-size:26px;font-weight:400;letter-spacing:1px;color:var(--brand-grey)}
.brand-rule{width:190px;height:1px;margin:8px auto 0;background:#c4c4c4}

.spread{position:absolute;top:259px;width:502px;height:370px;display:flex;background:var(--ink);
  box-shadow:0 6px 14px rgba(0,0,0,.25)}
.spread-outside{left:65px}
.spread-inside{left:619px}
.panel{position:relative;height:100%;overflow:hidden}

.bar{background:var(--orange);color:var(--ink);font-size:8px;font-weight:700;padding:2px 6px;margin:8px 0 5px;text-transform:uppercase;letter-spacing:.3px}
.copy{font-size:6.5px;line-height:1.55;color:var(--text-light);padding:0 8px}
.copy p{margin-bottom:5px}
.list{list-style:none;font-size:6.5px;line-height:1.7;padding:0 8px;color:var(--text-light)}
.list li::before{content:"› ";color:var(--orange)}

.photo{background:linear-gradient(160deg,#3a3f4a,#0d0f14)}
.photo-camera{position:absolute;left:10px;top:14px;width:148px;height:130px;
  background:radial-gradient(circle at 55% 50%,#3d3d3d 0%,#141414 65%)}
.mini-logo{position:absolute;left:0;right:0;top:218px;text-align:center}
.mini-logo .brand-mark{width:34px;height:34px}
.mini-logo .mini-name{display:block;margin-top:6px;font-size:12px;font-weight:600;color:var(--orange)}
.mini-logo .mini-url{display:block;margin-top:2px;font-size:5.5px;color:var(--text-dim)}

.cover-head{background:var(--white);height:70px;padding:10px 10px 0}
.cover-title{font-size:12px;font-weight:700;color:var(--orange-deep);font-style:normal}
.cover-tag{font-size:8px;color:#444;margin-top:3px;font-weight:600}
.cover-sub{font-size:6px;color:#777;margin-top:3px}
.cover-rule{height:3px;background:var(--orange)}
.photo-storm{height:297px;background:linear-gradient(180deg,#4b5567 0%,#7d8798 45%,#9aa1ad 70%,#3b3f47 100%)}

.photo-field{position:absolute;left:8px;right:8px;bottom:14px;height:96px;background:linear-gradient(180deg,#5a5f68,#2b2c30)}
.thumbs{position:absolute;left:8px;right:8px;bottom:14px;height:56px;display:flex;gap:4px}
.thumbs .photo{flex:1;background:linear-gradient(180deg,#8892a3,#3d434d)}

.parts{list-style:none;padding:10px 8px 0}
.parts li{display:flex;align-items:center;gap:6px;height:46px;border-bottom:1px solid #333}
.part-shot{width:52px;height:34px;background:radial-gradient(circle,#4a4a4a,#1b1b1b)}
.part-label{font-size:7px;font-weight:700;color:var(--orange)}
</style>
</head>
<body>

<header class="brand">
  <span class="brand-mark"></span>
  <span class="brand-name">DT Drevas</span>
  <div class="brand-rule"></div>
</header>

<section class="spread spread-outside">
  <div class="panel" style="width:175px;background:var(--panel)">
    <div class="bar">Specifications</div>
    <ul class="list">
      <li>Triggers on lightning and fireworks</li>
      <li>Day and night sensing modes</li>
      <li>Adjustable sensitivity dial</li>
      <li>Fast response under 1 ms</li>
      <li>Runs on two AA batteries</li>
      <li>Fits most camera hot shoes</li>
    </ul>
    <div class="bar">Compatibility</div>
    <div class="copy"><p>Works with major camera brands using a standard remote cable.</p></div>
    <div class="bar">Warranty</div>
    <div class="copy"><p>One year parts and labor coverage.</p></div>
    <div class="bar">In the Box</div>
    <div class="copy"><p>Unit, cable, pouch and quick guide.</p></div>
  </div>
  <div class="panel" style="width:168px;background:var(--ink)">
    <div class="photo-camera" role="img" aria-label="Sky Moth device mounted on a camera"></div>
    <div class="mini-logo">
      <span class="brand-mark"></span>
      <span class="mini-name">DT Drevas</span>
      <span class="mini-url">www.drevasystems.example</span>
    </div>
  </div>
  <div class="panel" style="width:159px">
    <div class="cover-head">
      <div class="cover-title">Sky Moth™</div>
      <div class="cover-tag">Built for every bold vision.</div>
      <div class="cover-sub">Trade show edition</div>
    </div>
    <div class="cover-rule"></div>
    <div class="photo-storm" role="img" aria-label="Lightning strikes over a stormy sky"></div>
  </div>
</section>

<section class="spread spread-inside">
  <div class="panel" style="width:173px;background:var(--panel)">
    <div class="bar">How It Works</div>
    <div class="copy">
      <p>The Sky Moth watches the scene for sudden changes in light and fires your shutter in an instant, catching strikes your reflexes would miss.</p>
      <p>Set it up on your tripod, aim at the storm and let it wait for the moment.</p>
    </div>
    <div class="bar">Field Tested</div>
    <div class="photo-field" role="img" aria-label="Photographer using the device in the field"></div>
  </div>
  <div class="panel" style="width:168px;background:var(--panel-2)">
    <div class="copy" style="padding-top:10px">
      <p>Designed by photographers for photographers, every control is placed where your hands expect it, even in the dark.</p>
      <p>Use it for fireworks, meteors, muzzle flashes and any fast burst of light after sunset.</p>
      <p>Visit www.drevasystems.example for sample images.</p>
    </div>
    <div class="thumbs">
      <div class="photo" role="img" aria-label="Sample lightning photograph"></div>
      <div class="photo" role="img" aria-label="Sample storm photograph"></div>
      <div class="photo" role="img" aria-label="Sample fireworks photograph"></div>
    </div>
  </div>
  <div class="panel" style="width:161px;background:var(--ink)">
    <ul class="parts">
      <li><div class="part-shot" role="img" aria-label="Sensor head close-up"></div><span class="part-label">Sensor Head</span></li>
      <li><div class="part-shot" role="img" aria-label="Lens port close-up"></div><span class="part-label">Lens Port</span></li>
      <li><div class="part-shot" role="img" aria-label="Control dial close-up"></div><span class="part-label">Control Dial</span></li>
      <li><div class="part-shot" role="img" aria-label="Mode switch close-up"></div><span class="part-label">Mode Switch</span></li>
      <li><div class="part-shot" role="img" aria-label="Cable jack close-up"></div><span class="part-label">Cable Jack</span></li>
      <li><div class="part-shot" role="img" aria-label="Mount foot close-up"></div><span class="part-label">Mount Foot</span></li>
    </ul>
  </div>
</section>

</body>
</html>
```